Postcard Design

www.lirvo.com.au
i am an occupational therapist and professionally trained coach. i work with children, parents and disability service providers to achieve brilliant outcomes for children with special needs.
http://www.lirvo.com.au/service/for-families
I need a postcard to give parents to promote our family service coaching service
A family service coach will work with you to set specific goals for your child, build a dream team, design and manage your child's highly effective therapy and educational team to ensure brilliant outcomes for your child..
KORLU - you have done my business card previously. they were great thank you.

```html
<!DOCTYPE html>
<html lang="en">
<head>
<meta charset="utf-8">
<title>Lirvo – Family Service Coach Postcard</title>
<link rel="stylesheet" href="https://fonts.googleapis.com/css2?family=Open+Sans:ital,wght@0,400;0,600;0,700;1,400&display=swap">
<style>
  :root{
    --page-bg:#e6e7e9;
    --card-white:#ffffff;
    --card-back:#f3f3f3;
    --brand-blue:#5b7fb5;
    --brand-blue-dark:#4a6aa3;
    --panel-blue:#b7c6da;
    --line-grey:#8c8c8c;
    --photo-warm-1:#e9dccb;
    --photo-warm-2:#c9a98a;
    --photo-cool:#6f8fb8;
    --photo-slate-1:#4a5a6e;
    --photo-slate-2:#7c8a99;
  }
  *{box-sizing:border-box;margin:0;padding:0}
  html,body{width:868px;height:1200px;overflow:hidden}
  body{background:var(--page-bg);font-family:"Open Sans",Arial,sans-serif;position:relative}

  /* Front of postcard */
  .card-front{position:absolute;left:49px;top:40px;width:691px;height:535px;background:var(--card-white);box-shadow:0 2px 6px rgba(0,0,0,.15)}
  .card-front svg{display:block;width:691px;height:535px}
  .front-heading{font-family:"Open Sans",Arial,sans-serif;font-weight:700;font-size:22px;fill:#fff}
  .front-web{font-family:"Open Sans",Arial,sans-serif;font-weight:700;font-size:18px;fill:#fff}
  .brand-name{font-family:"Open Sans",Arial,sans-serif;font-weight:600;font-size:34px;fill:var(--brand-blue)}
  .info-line{font-family:"Open Sans",Arial,sans-serif;font-size:13px;fill:var(--brand-blue-dark)}
  .info-line .url{font-weight:700}

  /* Back of postcard */
  .card-back{position:absolute;left:101px;top:615px;width:692px;height:535px;background:var(--card-back);box-shadow:0 2px 6px rgba(0,0,0,.15)}
  .back-header{position:absolute;left:0;top:0;width:430px;height:87px;background:var(--brand-blue);display:flex;align-items:center;padding-left:45px;gap:12px}
  .back-header .brand-dot{width:42px;height:42px;border-radius:50%;background:#fff}
  .back-header .brand-text{color:#fff;font-weight:600;font-size:34px;letter-spacing:.5px}
  .back-photo{position:absolute;left:0;top:94px;width:430px;height:182px;background:linear-gradient(120deg,var(--photo-slate-1),var(--photo-slate-2) 55%,var(--photo-slate-1))}
  .back-title{position:absolute;left:0;top:228px;width:430px;text-align:center;color:#fff;font-weight:700;font-size:24px}
  .back-panel{position:absolute;left:0;top:276px;width:430px;height:146px;background:var(--panel-blue);border-bottom-right-radius:12px;padding:16px 17px 0 26px}
  .back-panel p{color:#fff;font-size:13.4px;line-height:19px;text-align:justify}
  .back-panel .signature{position:absolute;right:75px;bottom:8px;font-style:italic;font-size:17px;color:#fff}
  .back-web{position:absolute;left:54px;top:422px;width:332px;height:48px;background:var(--brand-blue);border-radius:0 0 18px 18px;color:#fff;font-weight:700;font-size:19px;display:flex;align-items:center;justify-content:center}
  .stamp-box{position:absolute;left:589px;top:25px;width:84px;height:68px;border:1.5px solid var(--line-grey)}
  .address-lines{position:absolute;left:459px;top:172px;width:214px;list-style:none}
  .address-lines li{height:31px;border-top:1.5px solid var(--line-grey)}
  .back-info{position:absolute;left:0;bottom:12px;width:100%;text-align:center;font-size:13px;color:var(--brand-blue-dark)}
  .back-info .url{font-weight:700}
</style>
</head>
<body>

<section class="card-front" aria-label="Postcard front">
  <svg viewBox="0 0 691 535" xmlns="http://www.w3.org/2000/svg">
    <defs>
      <linearGradient id="familyPhotoTone" x1="0" y1="0" x2="1" y2="1">
        <stop offset="0" stop-color="var(--photo-warm-1)"/>
        <stop offset=".45" stop-color="var(--photo-warm-2)"/>
        <stop offset=".8" stop-color="var(--photo-cool)"/>
        <stop offset="1" stop-color="var(--photo-warm-1)"/>
      </linearGradient>
    </defs>
    <rect x="0" y="80" width="691" height="400" fill="url(#familyPhotoTone)" role="img" aria-label="Photo of a smiling family with two young children meeting a family service coach at home"/>
    <!-- top wave -->
    <path d="M0 0 H691 V104 Q560 78 420 104 Q300 128 0 108 Z" fill="var(--card-white)"/>
    <path d="M0 72 Q170 58 340 88 Q250 112 0 104 Z" fill="var(--brand-blue)"/>
    <path d="M0 110 Q300 130 420 106 Q560 80 691 106" fill="none" stroke="var(--panel-blue)" stroke-width="3"/>
    <text class="front-heading" x="60" y="99">Family Service Coach</text>
    <!-- logo -->
    <circle cx="510" cy="48" r="20" fill="var(--brand-blue)"/>
    <text class="brand-name" x="540" y="60">lirvo</text>
    <!-- bottom wave -->
    <path d="M0 448 Q160 470 330 470 Q520 468 691 436 V535 H0 Z" fill="var(--card-white)"/>
    <path d="M0 448 Q160 470 330 470" fill="none" stroke="var(--panel-blue)" stroke-width="3"/>
    <path d="M330 470 Q520 468 691 436 V492 Q560 494 440 486 Q380 480 330 470 Z" fill="var(--brand-blue)"/>
    <text class="front-web" x="428" y="484">www.lirvo.com.au</text>
    <text class="info-line" x="345.5" y="518" text-anchor="middle">visit our website for more information: <tspan class="url">http://www.lirvo.com.au/service/for-families</tspan></text>
  </svg>
</section>

<section class="card-back" aria-label="Postcard back">
  <header class="back-header">
    <span class="brand-dot"></span>
    <span class="brand-text">lirvo</span>
  </header>
  <div class="back-photo" role="img" aria-label="Photo of hands joining colourful jigsaw puzzle pieces"></div>
  <h2 class="back-title">Family Service Coach</h2>
  <div class="back-panel">
    <p>A family service coach will work with you to set specific goals for your child, build a dream team, design and manage your child's highly effective therapy and educational team to ensure brilliant outcomes for your child..</p>
    <span class="signature">Dana Hollis</span>
  </div>
  <div class="back-web">www.lirvo.com.au</div>
  <div class="stamp-box"></div>
  <ul class="address-lines"><li></li><li></li><li></li><li></li><li></li></ul>
  <p class="back-info">visit our website for more information: <span class="url">http://www.lirvo.com.au/service/for-families</span></p>
</section>

</body>
</html>
```